Waterproofing Construction company needs letterhead

I need a letterhead design for a commercial waterproofing construction company. We would like to see designs that are contemporary, clean, sleek and use our logo. Our current design is dated. I would also like a cover page (see example) that goes with our letterhead. I would like for the footer to have our address, website, and phone number

Target Market(s)

Customers, potential customers.

Font styles to use
Sans Serif

Requirements
Must have
• logo, website, address, phone numbers, only our colors, tahoma font
• PMS: 295C PMS: 2995C
• CMYK: 100/84/36/39 CMYK: 80/12/1/0
• RGB: 16/44/82 RGB: 0/167/224
• HEX#: #102C52 HEX#: #00A7E0
• Black & White: 100% Black & White: 32%
• Gray Scale: 90% Gray Scale: 32%
Nice to have
• Our "icon" logo attached would be nice somewhere on the page.

```html
<!DOCTYPE html>
<html lang="en">
<head>
<meta charset="utf-8">
<title>Halvern Letterhead and Cover</title>
<link href="https://fonts.googleapis.com/css2?family=Roboto:wght@300;400;700;900&family=Roboto+Condensed:wght@400;700&display=swap" rel="stylesheet">
<style>
  :root {
    --navy: #102C52;
    --navy-deep: #13285a;
    --cyan: #00A7E0;
    --cyan-light: #1ab2ea;
    --stage: #e4e4e4;
    --ink: #555;
    --white: #ffffff;
  }
  * { margin: 0; padding: 0; box-sizing: border-box; }
  html, body { width: 1200px; height: 597px; overflow: hidden; }
  body {
    position: relative;
    background: var(--stage);
    font-family: "Roboto", Tahoma, sans-serif;
  }
  .page {
    position: absolute;
    top: 43px;
    width: 360px;
    height: 506px;
    overflow: hidden;
    box-shadow: 0 1px 4px rgba(0,0,0,.25);
  }

  /* Letterhead */
  .letterhead { left: 36px; background: linear-gradient(90deg, #fff 0%, #f1f1f1 100%); }
  .brand { position: absolute; }
  .brand-name {
    font-weight: 900;
    color: var(--navy);
    letter-spacing: -0.5px;
    line-height: 1;
  }
  .brand-tag {
    font-weight: 700;
    color: var(--navy);
    letter-spacing: 0.1px;
    white-space: nowrap;
  }
  .letterhead .brand { left: 33px; top: 41px; }
  .letterhead .brand-name { font-size: 29px; }
  .letterhead .brand-tag { font-size: 5.6px; margin-top: 1px; }

  .salutation {
    position: absolute; left: 32px; top: 134px;
    font-size: 10px; font-weight: 300; color: #444;
  }
  .letter-body {
    position: absolute; left: 32px; top: 159px; width: 298px;
    font-size: 5.3px; line-height: 7.7px; font-weight: 300; color: var(--ink);
  }
  .letter-body p { margin-bottom: 7px; }
  .closing {
    position: absolute; left: 32px; top: 322px;
    font-size: 5.3px; font-weight: 300; color: var(--ink);
  }
  .signature {
    position: absolute; left: 28px; top: 344px; width: 66px; height: 28px;
    background: rgba(45, 95, 170, .12); border-radius: 3px;
  }
  .letter-footer {
    position: absolute; left: 12px; top: 458px; right: 0; height: 37px;
    border-radius: 19px 0 0 19px;
    background: linear-gradient(90deg, #11a3e0 0%, #1479c4 45%, var(--navy) 100%);
    color: var(--white);
    padding: 6px 0 0 19px;
    font-size: 5.4px; line-height: 8px;
  }
  .contact-line { display: flex; align-items: center; gap: 3px; white-space: nowrap; }
  .contact-line svg { width: 5px; height: 5px; fill: currentColor; }
  .contact-line .gap { width: 2px; }

  /* Cover */
  .cover { left: 422px; }
  .cover-photo {
    position: absolute; inset: 0;
    background: linear-gradient(180deg, #bfbfbf 0%, #8d8d8d 35%, #4a4a4a 70%, #2a2a2a 100%);
  }
  .cover .brand { left: 30px; top: 26px; }
  .cover .brand-name { font-size: 40px; }
  .cover .brand-tag { font-size: 7.6px; margin-top: 1px; }
  .anniversary-badge {
    position: absolute; left: 234px; top: 26px; width: 98px; height: 25px;
    border: 2px solid var(--navy); border-radius: 4px;
    background: rgba(255,255,255,.35);
  }
  .cover-statement {
    position: absolute; left: 6px; right: 0; top: 393px; height: 73px;
    border-radius: 36px 0 0 36px;
    background: rgba(0, 155, 220, .85);
    color: var(--white);
    font-size: 8.6px; line-height: 10.5px; text-align: center;
    padding: 10px 20px 0 26px;
  }
  .cover-url {
    position: absolute; left: 0; right: 0; top: 480px;
    text-align: center; color: var(--white);
    font-size: 11px; letter-spacing: 6px;
  }

  /* Back page */
  .back { left: 808px; background: var(--navy-deep); }
  .back-frame {
    position: absolute; inset: 10px;
    border: 1.5px solid var(--cyan);
  }
  .back-content {
    position: absolute; left: 0; right: 0; top: 204px;
    text-align: center; color: var(--white);
  }
  .back-title {
    font-family: "Roboto Condensed", Tahoma, sans-serif;
    font-weight: 700; font-size: 14.5px; color: var(--cyan-light);
    letter-spacing: .2px;
  }
  .rule { width: 20px; height: 1px; background: var(--white); margin: 10px auto; }
  .rep-name { font-size: 8.2px; font-weight: 700; color: var(--cyan-light); line-height: 10px; }
  .rep-line { font-size: 8.6px; line-height: 10px; }
  .rep-email { font-style: italic; }
  .back-address { font-size: 5.4px; line-height: 8px; }
  .back-address .contact-line { justify-content: center; }
  .back-address svg { fill: var(--cyan-light); }
</style>
</head>
<body>

  <section class="page letterhead">
    <div class="brand">
      <div class="brand-name">HALVERN</div>
      <div class="brand-tag">WATERPROOFING • RESTORATION</div>
    </div>

    <p class="salutation">Dear Mr. Smith,</p>

    <div class="letter-body">
      <p>Thank you for the chance to review the roof and deck areas at your building last week. Our crew has prepared a full report on each leak point, with notes on the membrane, flashing, drain lines and parapet caps. Photos of every area are included, along with moisture readings taken at each test spot. We are glad to walk the site with your team at any time that suits your schedule, and we can meet with the owners as well.</p>
      <p>The attached plan outlines three options for repair, from a targeted sealant program to a complete coating system over the full roof. Each option lists the scope, schedule, crew size and expected service life, so you can compare them side by side before you decide. We have also noted which items should be handled first to stop water entry before the fall rains, and which can wait until the next budget year.</p>
      <p>Work can begin within two weeks of approval and will be staged to keep entrances, loading docks and parking areas open for tenants. Our foreman will send a short update at the end of each day, with photos of the work done and any items that need your input. All materials are stored on site in a locked area, and the crew will clean up each evening. Every job is backed by our written warranty on labor and materials, and we return for a free check after the first year.</p>
      <p>Please call or write with any questions about the plan or the pricing. We can adjust the scope to fit your needs and timeline. We look forward to working with you on this project and thank you again for your trust in our team.</p>
    </div>

    <p class="closing">Sincerely,</p>
    <div class="signature" role="img" aria-label="Handwritten signature of Paul Ward"></div>

    <footer class="letter-footer">
      <div>PO Box 410, Linden, OR 97000</div>
      <div class="contact-line">
        <svg viewBox="0 0 10 10"><path d="M2 0.5l2 2.2-1 1.2a6 6 0 003 3l1.2-1 2.2 2-1 1.8C4.5 9.5.5 5.5.2 1.5z"/></svg>
        <span>(800) 555-0142</span><span class="gap"></span>
        <svg viewBox="0 0 10 10"><rect x="2" y="0.5" width="6" height="3"/><rect x="0" y="3.5" width="10" height="4" rx="1"/><rect x="2" y="6.5" width="6" height="3"/></svg>
        <span>(555) 555-0178</span><span class="gap"></span>
        <svg viewBox="0 0 10 10"><circle cx="5" cy="5" r="4.5"/></svg>
        <span>www.HalvernWP.com</span>
      </div>
      <div>Oregon | Washington | Idaho</div>
    </footer>
  </section>

  <section class="page cover">
    <div class="cover-photo" role="img" aria-label="Black and white photo looking up at glass skyscrapers against a cloudy sky"></div>
    <div class="brand">
      <div class="brand-name">HALVERN</div>
      <div class="brand-tag">WATERPROOFING • RESTORATION</div>
    </div>
    <div class="anniversary-badge"></div>
    <div class="cover-statement">
      Halvern is committed to building lasting and valuable business relationships, with all of our clients by consistently providing the value and service that, keeps Halvern at the forefront of our industry. This commitment makes Halvern, the premier provider for quality commercial waterproofing, restoration, and exterior maintenance.
    </div>
    <div class="cover-url">WWW.HALVERNWP.COM</div>
  </section>

  <section class="page back">
    <div class="back-frame"></div>
    <div class="back-content">
      <h2 class="back-title">CONTACT US</h2>
      <div class="rule"></div>
      <div class="rep-name">MARC DELANEY</div>
      <div class="rep-line">Project Developer</div>
      <div class="rep-line rep-email">marc@halvernwp.com</div>
      <div class="rep-line">555-240-1187</div>
      <div class="rule"></div>
      <div class="back-address">
        <div>PO Box 410, Linden, OR 97000</div>
        <div class="contact-line">
          <svg viewBox="0 0 10 10"><path d="M2 0.5l2 2.2-1 1.2a6 6 0 003 3l1.2-1 2.2 2-1 1.8C4.5 9.5.5 5.5.2 1.5z"/></svg>
          <span>(800) 555-0142</span><span class="gap"></span>
          <svg viewBox="0 0 10 10"><rect x="2" y="0.5" width="6" height="3"/><rect x="0" y="3.5" width="10" height="4" rx="1"/><rect x="2" y="6.5" width="6" height="3"/></svg>
          <span>(555) 555-0178</span><span class="gap"></span>
          <svg viewBox="0 0 10 10"><circle cx="5" cy="5" r="4.5"/></svg>
          <span>www.HalvernWP.com</span>
        </div>
        <div>Oregon | Washington | Idaho</div>
      </div>
    </div>
  </section>

</body>
</html>
```